Yummy Website Re-Design

We have a good website but no VERY GOOD :)

We would like improve the user experience, in shopping page particularly.

Target Market(s)

people 25-40 70% of girl (actually)

Industry/Entity Type

Shopping

Requirements
Must have
• Redesign of www.brunolake.ch
Same colors
Same logotype

1) Homepage
- With highlight product / offer (large display!)
- Space to explain the concept
- Delicious button call-to-action for order a breakfast

2) THE CONCEPT
- Page for explain the concept and team pictures (3persons)

3) COMPOSE !
- Shopping page with, on the top, the X package we offer (business pack, st valentine, christmas, family, etc.) (slider?)

- Then, the products (grid?) classified into categories, we would'like to display one photo / item, the name, the weight and the price.

If you want to add the product, you must choose the number of elements and add to cart

Please, suscribe and test the order process to view all step

4) DELIVERY ZONES
- Page with map of different delivery rate and possibility

5) FAQ

X) Footer with the same information what www.brunolake.ch

Yummy, delicious design (we delivery very delicious breakfast @home).

LET'S EXPLODE YOUR CREATIVITY WITH THIS WORDS : YUMMY, DELICIOUS, SWEET.

```html
<!DOCTYPE html>
<html lang="en">
<head>
<meta charset="utf-8">
<title>Bruno Lake — Breakfast delivered at home</title>
<link rel="stylesheet" href="https://fonts.googleapis.com/css2?family=Cinzel:wght@400;700&family=Crimson+Text:ital,wght@0,400;0,600;1,400&display=swap">
<style>
:root{
  --bar:#1b1b1b;
  --panel:#1d1d1d;
  --panel-edge:#2a2a2a;
  --tan:#c49a6c;
  --tan-dark:#8a6440;
  --gold:#d9a23a;
  --gold-dark:#b3741a;
  --cream:#f4efe6;
  --footer-top:#2b1d12;
  --footer-bottom:#5a3d24;
  --field:#6e4c2d;
  --copy:#d98a3a;
  --texture:#4a4038;
}
*{box-sizing:border-box;margin:0;padding:0}
html,body{width:1200px;height:749px;overflow:hidden;background:var(--bar)}
.page{position:relative;width:1200px;height:749px;overflow:hidden;font-family:"Crimson Text",Georgia,serif}

.hero-photo{position:absolute;left:0;top:51px;width:1200px;height:583px;
  background:
    radial-gradient(ellipse 240px 160px at 120px 130px,#e8b430 0%,rgba(232,180,48,0) 70%),
    radial-gradient(ellipse 230px 260px at 1050px 430px,#f0a828 0%,rgba(240,168,40,0) 70%),
    radial-gradient(ellipse 420px 300px at 760px 330px,#f3ede4 0%,rgba(243,237,228,0) 75%),
    radial-gradient(ellipse 260px 120px at 370px 580px,#c07a30 0%,rgba(192,122,48,0) 75%),
    linear-gradient(120deg,#6a5240 0%,#a8947c 40%,#d8cfc2 60%,#7a6450 100%)}

.top-bar{position:absolute;left:0;top:0;width:1200px;height:51px;background:var(--bar)}
.search-strip{position:absolute;left:406px;top:51px;width:794px;height:37px;background:rgba(70,60,52,.55)}

.brand{position:absolute;left:144px;top:0;width:262px;height:130px;
  background:linear-gradient(160deg,#2a2a2a,#0e0e0e);box-shadow:0 4px 10px rgba(0,0,0,.6);
  border-bottom:2px solid var(--tan-dark);display:flex;align-items:center;justify-content:center}
.brand-name{font-family:"Cinzel",serif;font-weight:400;font-size:34px;color:var(--tan);letter-spacing:1px}

.main-nav{position:absolute;left:434px;top:5px;height:42px;display:flex;border-bottom:1px solid var(--tan-dark)}
.main-nav a{font-family:"Cinzel",serif;font-size:17px;color:var(--tan);text-decoration:none;
  padding:8px 14px 0;border-left:1px solid #3a3a3a;height:42px;line-height:26px}

.search{position:absolute;left:818px;top:56px;width:179px;height:23px;background:#2a2a2a;
  border:1px solid #444;display:flex;align-items:center;padding:0 6px}
.search span{flex:1;font-style:italic;font-size:11px;color:var(--tan)}
.search svg{width:11px;height:11px}

.offer{position:absolute;left:147px;top:251px;width:545px;height:238px;background:var(--panel);
  border:1px solid var(--panel-edge);box-shadow:0 6px 14px rgba(0,0,0,.5);text-align:center;color:var(--cream)}
.offer-band{position:absolute;height:7px;background:var(--texture)}
.offer h1{font-family:"Cinzel",serif;font-weight:400;font-size:50px;line-height:52px;margin-top:26px;
  text-shadow:0 0 1px #fff}
.offer p{font-family:"Cinzel",serif;font-size:21px;line-height:24px;margin-top:10px}
.offer p strong{font-weight:400;font-size:24px}

.order-button{position:absolute;left:291px;top:459px;width:246px;height:55px;border-radius:8px;
  background:linear-gradient(#f0b53c,var(--gold-dark));border:3px solid #8a5a1a;
  box-shadow:0 4px 8px rgba(0,0,0,.5);font-family:"Cinzel",serif;font-weight:700;font-size:18px;
  color:#2a1a0a;display:flex;align-items:center;justify-content:center;text-decoration:none}

.connect{position:absolute;left:871px;top:606px;width:157px;height:28px;background:#fff;
  display:flex;align-items:center;padding:0 5px;gap:4px}
.connect em{font-size:11px;color:var(--tan-dark);margin-right:9px}
.connect i{display:block;width:21px;height:19px;background:#a8a086}

.site-footer{position:absolute;left:0;top:634px;width:1200px;height:115px;
  background:linear-gradient(var(--footer-top),var(--footer-bottom))}
.footer-rule{position:absolute;left:295px;top:7px;width:650px;height:1px;background:var(--tan-dark)}
.footer-links{position:absolute;left:181px;top:39px;font-size:14px;color:var(--cream)}
.copyright{position:absolute;left:182px;top:66px;font-family:Arial,sans-serif;font-size:10px;color:var(--copy)}
.newsletter h2{position:absolute;left:506px;top:25px;font-weight:600;font-size:17px;color:var(--cream)}
.newsletter-field{position:absolute;left:504px;top:48px;width:319px;height:29px;background:var(--field);
  font-size:14px;color:var(--cream);padding:5px 8px}
.newsletter-send{position:absolute;left:821px;top:46px;width:33px;height:33px;border-radius:50%;
  background:#000;border:2px solid #3a2a1a;display:flex;align-items:center;justify-content:center}
.footer-brand{position:absolute;left:883px;top:32px;width:145px;text-align:center;
  font-family:"Cinzel",serif;font-size:24px;color:var(--tan)}
</style>
</head>
<body>
<div class="page">
  <div class="hero-photo" role="img" aria-label="Photo of a breakfast tray with coffee, milk jug, orange juice, a croissant and a yellow flower"></div>

  <header>
    <div class="top-bar"></div>
    <div class="search-strip"></div>
    <div class="brand"><span class="brand-name">Bruno Lake</span></div>
    <nav class="main-nav">
      <a href="#">Home</a><a href="#">The Concept</a><a href="#">Compose!</a><a href="#">Delivery Zones</a><a href="#">FAQ</a>
    </nav>
    <div class="search"><span>Search Products &amp; Recipes</span>
      <svg viewBox="0 0 12 12"><circle cx="7" cy="5" r="3.5" fill="none" stroke="#c49a6c" stroke-width="1.5"/><line x1="4.5" y1="7.5" x2="1" y2="11" stroke="#c49a6c" stroke-width="1.5"/></svg>
    </div>
  </header>

  <div class="offer-band" style="left:147px;top:242px;width:545px"></div>
  <div class="offer-band" style="left:149px;top:481px;width:543px"></div>
  <section class="offer">
    <h1>Yummy<br>Delicious, Sweet</h1>
    <p>We deliver very delicious breakfast<br>@ <strong>HOME</strong></p>
  </section>
  <a class="order-button" href="#">Order a Breakfast</a>

  <div class="connect"><em>Connect</em><i></i><i></i><i></i><i></i></div>

  <footer class="site-footer">
    <div class="footer-rule"></div>
    <div class="footer-links">Welcome &nbsp;-&nbsp; Prepare Your Lil BF &nbsp;-&nbsp; Delivery Area</div>
    <div class="copyright">Copyright © 2012 BrunoLake. All rights reserved.</div>
    <div class="newsletter">
      <h2>Subscribe To Our Newsletter</h2>
      <div class="newsletter-field">Enter Your Email Address</div>
      <div class="newsletter-send"><svg width="10" height="14" viewBox="0 0 10 14"><path d="M2 1l6 6-6 6" fill="none" stroke="#fff" stroke-width="2"/></svg></div>
    </div>
    <div class="footer-brand">Bruno Lake</div>
  </footer>
</div>
</body>
</html>
```